Youth deer hunt give away flyer.

We need a flyer designed for a youth deer hunt giveaway that we are doing. We are an Illinois whitetail deer hunting outfitter. We house and feed our clients as well as providing them with a guided deer hunt. It needs to include images as well as details about the giveaway. Im looking for a proffesional, looking flyer

Target Market(s)

rednecks, hunters

Industry/Entity Type

Hunting

Font styles to use
Serif
Sans Serif

Colors
000000
dbdbdb
ffffff
474747

Requirements
Must have
• not sure
Nice to have
• not sure
Should not have
• not sure

```html
<!DOCTYPE html>
<html lang="en">
<head>
<meta charset="utf-8">
<title>Harlan Ridge Outfitting – 2018 Youth Firearm Hunt</title>
<link rel="stylesheet" href="https://fonts.googleapis.com/css2?family=Tinos:wght@400;700&family=Arimo:wght@400;700&display=swap">
<style>
  :root {
    --black: #000000;
    --ink: #1a1a1a;
    --light: #dbdbdb;
    --white: #ffffff;
    --slate: #474747;
    --divider: #777777;
    --forest-dark: #2a1c10;
    --forest-mid: #5a3f22;
    --forest-warm: #8a6232;
  }
  * { margin: 0; padding: 0; box-sizing: border-box; }
  html, body { width: 900px; height: 1200px; overflow: hidden; background: var(--white); }
  .flyer {
    position: relative; width: 900px; height: 1200px; overflow: hidden;
    background: var(--light); font-family: "Tinos", "Times New Roman", serif; color: var(--ink);
  }
  .hero-photo {
    position: absolute; left: 0; top: 0; width: 900px; height: 600px;
    background: linear-gradient(160deg, var(--forest-mid) 0%, var(--forest-dark) 45%, var(--forest-warm) 80%, var(--forest-dark) 100%);
  }
  .shapes { position: absolute; left: 0; top: 0; }
  .photo-circle {
    position: absolute; width: 226px; height: 226px; border-radius: 50%;
    border: 8px solid var(--white); box-shadow: 0 3px 8px rgba(0,0,0,.35);
  }
  .photo-circle--youth { left: 302px; top: 360px; background: linear-gradient(180deg, #1b1b1b 0%, #3d3a2c 55%, #6e6a52 100%); }
  .photo-circle--cabin { left: 630px; top: 352px; background: linear-gradient(150deg, #d39a5a 0%, #a8692f 50%, #6b4420 100%); }

  .about { position: absolute; left: 33px; top: 598px; width: 805px; }
  .about__title {
    font-size: 26px; font-weight: 700; display: inline-block;
    border-bottom: 1.5px solid var(--slate); padding-right: 28px; line-height: 1.1; margin-bottom: 4px;
  }
  .about p { font-size: 14.6px; line-height: 1.2; }

  .promo-banner {
    position: absolute; left: 0; top: 751px; width: 443px; height: 36px;
    background: var(--black); color: var(--white); border-radius: 0 18px 18px 0;
    font-size: 24px; font-weight: 700; padding-left: 33px; line-height: 36px;
    box-shadow: 0 5px 6px rgba(0,0,0,.35);
  }

  .details { position: absolute; top: 800px; left: 33px; display: flex; align-items: flex-start; }
  .details__col { list-style: none; font-size: 18px; font-weight: 700; line-height: 21px; }
  .details__col li { position: relative; padding-left: 18px; margin-bottom: 20px; }
  .details__col li::before { content: "◆"; position: absolute; left: 0; top: 0; font-size: 10px; }
  .details__col--a { width: 332px; padding-right: 40px; }
  .details__col--b { width: 282px; height: 97px; padding-left: 27px; padding-right: 60px; border-left: 1.5px dotted var(--divider); }
  .details__col--c { height: 97px; padding-left: 35px; border-left: 1.5px dotted var(--divider); }

  .call {
    position: absolute; left: 272px; top: 930px; font-family: "Arimo", Arial, sans-serif;
    font-size: 31px; color: var(--ink); line-height: 60px; white-space: nowrap;
  }
  .call strong { font-family: "Tinos", "Times New Roman", serif; font-size: 56px; font-weight: 700; margin-left: 10px; vertical-align: -3px; }

  .brand { position: absolute; left: 16px; top: 1133px; width: 230px; text-align: center; color: var(--white); }
  .brand__name { font-size: 27px; letter-spacing: 1px; line-height: 1; }
  .brand__tag { font-size: 11px; letter-spacing: 4px; margin-top: 5px; }

  .contact { position: absolute; left: 283px; top: 1064px; color: var(--white); font-size: 15.5px; list-style: none; }
  .contact li { display: flex; align-items: flex-start; gap: 13px; line-height: 18px; }
  .contact__address { margin-bottom: 10px; }
  .contact__web { margin-bottom: 24px; }
  .contact svg { flex: none; margin-top: 1px; }

  .social { position: absolute; left: 652px; top: 1150px; display: flex; gap: 12px; }
  .social span { width: 20px; height: 20px; border-radius: 50%; background: var(--white); }
</style>
</head>
<body>
<main class="flyer">
  <div class="hero-photo" role="img" aria-label="Hunter kneeling in autumn woods behind a large trophy whitetail buck"></div>

  <svg class="shapes" width="900" height="1200" viewBox="0 0 900 1200" aria-hidden="true">
    <path d="M0 528 Q430 458 900 430 L900 1200 L0 1200 Z" fill="var(--black)"/>
    <path d="M0 578 Q440 490 900 452 L900 1200 L0 1200 Z" fill="var(--light)"/>
    <path d="M900 927 L694 1095 L900 1152 Z" fill="var(--slate)"/>
    <path d="M0 927 L900 1152 L900 1200 L0 1200 Z" fill="var(--black)"/>
    <path d="M900 920 L686 1097 L900 1160" fill="none" stroke="var(--black)" stroke-width="5"/>
  </svg>

  <div class="photo-circle photo-circle--youth" role="img" aria-label="Youth hunter and guide in blaze orange with a harvested buck at night"></div>
  <div class="photo-circle photo-circle--cabin" role="img" aria-label="Interior of the wood-paneled private hunting cabin"></div>

  <section class="about">
    <h2 class="about__title">About us</h2>
    <p>Harlan Ridge Outfitting is a family owned and operated deer hunting outfitter located in Morgan and Scott Counties in west central Illinois. We provide low pressure, trophy whitetail hunts on privately owned farms across the region. The Harlans are lifelong residents and hunters of Morgan County, with the family farm being established well over 150 years ago.</p>
    <p>To go along with guiding deer and turkey hunters, we also offer a wide variety of professional hunting services that include whitetail land consulting, scouting services, CRP and food plot plantings and more.</p>
  </section>

  <h2 class="promo-banner">2018 YOUTH FIREARM HUNT</h2>

  <div class="details">
    <ul class="details__col details__col--a">
      <li>Guided shotgun hunt on strictly managed properties.</li>
      <li>4 night stay in our private cabin that include meals for 2 parents and the child.</li>
    </ul>
    <ul class="details__col details__col--b">
      <li>Ground blinds in place</li>
      <li>Permit and license fees are the hunters responsibility.</li>
    </ul>
    <ul class="details__col details__col--c">
      <li>October 6-8, 2018</li>
    </ul>
  </div>

  <p class="call">Call Us: <strong>(555)014-2290</strong></p>

  <div class="brand">
    <div class="brand__name">HARLAN RIDGE</div>
    <div class="brand__tag">OUTFITTING</div>
  </div>

  <ul class="contact">
    <li class="contact__address">
      <svg width="14" height="18" viewBox="0 0 14 18"><path d="M7 1a6 6 0 0 0-6 6c0 4.5 6 10 6 10s6-5.5 6-10a6 6 0 0 0-6-6z" fill="none" stroke="var(--white)" stroke-width="1.6"/><circle cx="7" cy="7" r="2.2" fill="var(--white)"/></svg>
      <span>4870 Harlan Road<br>Millbrook, Illinois 62000</span>
    </li>
    <li class="contact__web">
      <svg width="16" height="16" viewBox="0 0 16 16"><circle cx="8" cy="8" r="7" fill="none" stroke="var(--white)" stroke-width="1.5"/><ellipse cx="8" cy="8" rx="3" ry="7" fill="none" stroke="var(--white)" stroke-width="1.2"/><path d="M1 8h14" stroke="var(--white)" stroke-width="1.2"/></svg>
      <span>www.harlanridgeoutfitting.com</span>
    </li>
    <li class="contact__email">
      <svg width="16" height="16" viewBox="0 0 16 16"><circle cx="8" cy="8" r="7.5" fill="var(--white)"/><rect x="4" y="5" width="8" height="6" fill="none" stroke="var(--black)" stroke-width="1.2"/><path d="M4 5l4 3.5L12 5" fill="none" stroke="var(--black)" stroke-width="1.2"/></svg>
      <span>hello@harlanridgeoutfitting.com</span>
    </li>
  </ul>

  <div class="social" aria-label="Social media"><span></span><span></span></div>
</main>
</body>
</html>
```